New local Orchid nursery branding

We need a business card designed for our small local company in Darwin, Australia that grows orchids, called Blooms at Carrow.
We will be running private sales from our property, and handing these out at local events for perspective customers.

We would like to see designs that are simple, and able to be used with minimal colours and containing an orchid, preferably a stylised representation instead of a photo.
The eventual hope is to take this into larger formats to create our company logo/branding etc, but for now we just need business cards.

Target Market(s)

Local Orchid

Industry/Entity Type

Business

Contact Information for Business Card

Company Name
Logo
Name
Phone Number
Street Address
Email Address (less prominent than rest of the text)

Font styles to use
Sans Serif

Requirements
Must have
• Name of the company, which is Blooms at Carrow
Nice to have
• stylised orchid logo
Should not have
• too many colours

```html
<!DOCTYPE html>
<html lang="en">
<head>
<meta charset="utf-8">
<title>Blooms at Carrow — Business Card</title>
<link rel="stylesheet" href="https://fonts.googleapis.com/css2?family=Questrial&display=swap">
<style>
  :root {
    --page-bg: #e9e7ea;
    --card-purple: #7a4a9e;
    --card-cream: #fdf1ec;
    --edge-peach: #f4bfa6;
    --bloom-purple: #7c4aa0;
    --text-white: #ffffff;
  }
  * { margin: 0; padding: 0; box-sizing: border-box; }
  html, body {
    width: 1200px;
    height: 720px;
    overflow: hidden;
    background: var(--page-bg);
    font-family: "Questrial", "Century Gothic", sans-serif;
  }
  .business-card {
    position: absolute;
    left: 100px;
    top: 74px;
    width: 1000px;
    height: 572px;
    background: var(--card-purple);
    overflow: hidden;
    box-shadow: 0 10px 30px rgba(0, 0, 0, 0.18);
  }
  .card-art {
    position: absolute;
    inset: 0;
    width: 1000px;
    height: 572px;
  }
  .brand {
    position: absolute;
    left: 52px;
    top: 46px;
    display: flex;
    align-items: center;
    gap: 12px;
    color: var(--text-white);
  }
  .brand-name {
    font-size: 44px;
    letter-spacing: 1px;
    line-height: 1;
  }
  .brand-dot {
    width: 18px;
    height: 18px;
    border-radius: 50%;
    background: var(--text-white);
  }
  .contact-list {
    position: absolute;
    left: 58px;
    top: 150px;
    list-style: none;
    color: var(--text-white);
    font-size: 25px;
    line-height: 1;
  }
  .contact-item {
    display: flex;
    align-items: center;
    gap: 18px;
    height: 33px;
  }
  .contact-item.address { margin-bottom: 20px; }
  .contact-icon {
    width: 17px;
    height: 17px;
    flex: none;
    fill: var(--text-white);
  }
  .icon-spacer { width: 17px; flex: none; }
</style>
</head>
<body>
  <div class="business-card">
    <svg class="card-art" viewBox="0 0 1000 572">
      <defs>
        <clipPath id="cream-clip">
          <path d="M322 572 C 450 345, 710 208, 1000 170 L 1000 572 Z"/>
        </clipPath>
        <radialGradient id="bloom-fill" cx="0.5" cy="0.5" r="0.5">
          <stop offset="0" stop-color="var(--bloom-purple)" stop-opacity="0.9"/>
          <stop offset="0.6" stop-color="var(--bloom-purple)" stop-opacity="0.55"/>
          <stop offset="1" stop-color="var(--bloom-purple)" stop-opacity="0"/>
        </radialGradient>
      </defs>
      <path class="cream-edge" d="M300 572 C 430 330, 700 190, 1000 150 L 1000 572 Z" fill="var(--edge-peach)"/>
      <path class="cream-panel" d="M322 572 C 450 345, 710 208, 1000 170 L 1000 572 Z" fill="var(--card-cream)"/>
      <g clip-path="url(#cream-clip)">
        <ellipse class="orchid-spray" cx="780" cy="420" rx="240" ry="190"
                 fill="url(#bloom-fill)"
                 role="img" aria-label="Stylised purple orchid spray with several open blooms on an arching stem"/>
      </g>
    </svg>

    <div class="brand">
      <span class="brand-name">Blooms at Carrow</span>
      <span class="brand-dot"></span>
    </div>

    <ul class="contact-list">
      <li class="contact-item address">
        <svg class="contact-icon" viewBox="0 0 24 24"><path d="M12 2a7 7 0 0 0-7 7c0 5 7 13 7 13s7-8 7-13a7 7 0 0 0-7-7zm0 9.5A2.5 2.5 0 1 1 12 6.5a2.5 2.5 0 0 1 0 5z"/></svg>
        <span>company address</span>
      </li>
      <li class="contact-item phone">
        <svg class="contact-icon" viewBox="0 0 24 24"><path d="M6.6 10.8a15 15 0 0 0 6.6 6.6l2.2-2.2a1 1 0 0 1 1-.25 11.4 11.4 0 0 0 3.6.57 1 1 0 0 1 1 1V20a1 1 0 0 1-1 1A17 17 0 0 1 3 4a1 1 0 0 1 1-1h3.5a1 1 0 0 1 1 1c0 1.25.2 2.45.57 3.57a1 1 0 0 1-.25 1z"/></svg>
        <span>0123 45 678</span>
      </li>
      <li class="contact-item mobile">
        <span class="icon-spacer"></span>
        <span>0111 22 33 4455</span>
      </li>
      <li class="contact-item email">
        <svg class="contact-icon" viewBox="0 0 24 24"><path d="M3 5h18v14H3z"/></svg>
        <span>email@Companyname.com</span>
      </li>
      <li class="contact-item web">
        <svg class="contact-icon" viewBox="0 0 24 24"><circle cx="12" cy="12" r="9"/></svg>
        <span>www.companyname.com</span>
      </li>
    </ul>
  </div>
</body>
</html>
```